Restaurant Needs a Flyer Design for a Cocktail Competition

We are a Chinese restaurant specializing in hot pot cuisine. More information about our specialty and product line can be found on our website: www.brimbasket.com.
We are expanding our bar menu and plan to hold a competition between local bartenders to craft new signature sake cocktails for our restaurant. We need someone to design a flyer that can be distributed to local bars and restaurants in order to catch their interest.
For the name of the competition, we were considering something along the lines of "Summer of Sake - Brimba Sketto's Cocktail Competition". However, more consideration will be given to designs that come up with an original, creative headline. The headline must reference that it is a "sake cocktail" competition to avoid any confusion.
The overall look of the flyer should be fun and eye-catching.
The information that we need included on the front of the flyer (not in this wording or order) is as follows:
1. Name of our restaurant, website, and location
2. The name of the competition
3. Submissions must be submitted to this email address: brimbasket1@quillmarn.com
4. The deadline for submissions is July 31st, 2015
5. Images to accompany the text as well as our logo
6. Eight finalists will be chosen by the restaurant's staff and the top three will be chosen by customer vote.
7. The top three will be awarded prizes:
a. Grand Prize Winner: The choice of either a
"Winner's Dinner" for them and their entire staff
OR a cash prize of $300
b. 2nd Prize Winner: $100 cash prize AND $100
Brimba Sketto gift card
c. 3rd Prize Winner: $100 Brimba Sketto gift card
8. ALL three winners will receive a credit under their winning drink on our menu - their bar/restaurant will be credited on the menu as well
9. The eight finalists will be chosen by August 10th, 2015 and the three winners will be chosen by August 31st, 2015.
On the back of the flyer we will include a list of our submission guidelines and contest rules. Those guidelines and rules are included as attachments at the bottom along with our logo.

```html
<!DOCTYPE html>
<html lang="en">
<head>
<meta charset="utf-8">
<title>Brimba Sketto Sake Cocktail Competition – Rules and Guidelines</title>
<link rel="stylesheet" href="https://fonts.googleapis.com/css2?family=Hind:wght@500&display=swap">
<style>
  :root {
    --ink-night: #0a0d09;
    --bottle-green: #5fbf3a;
    --bottle-mint: #a9e6a0;
    --glass-blue: #1d2f6b;
    --amber-warm: #6a4a22;
    --text-white: #ffffff;
    --heading-red: #e0201c;
  }
  html, body {
    margin: 0;
    padding: 0;
    width: 1200px;
    height: 789px;
    overflow: hidden;
    background: var(--ink-night);
  }
  .flyer-back {
    position: relative;
    width: 1200px;
    height: 789px;
    overflow: hidden;
    font-family: "Hind", "Arial Narrow", sans-serif;
    font-weight: 500;
    text-transform: uppercase;
    color: var(--text-white);
  }
  .sake-backdrop {
    position: absolute;
    inset: 0;
    background:
      radial-gradient(ellipse 110px 260px at 505px 520px, rgba(95,191,58,0.75), transparent 75%),
      radial-gradient(ellipse 150px 300px at 805px 470px, rgba(169,230,160,0.7), transparent 75%),
      radial-gradient(ellipse 90px 220px at 1020px 430px, rgba(29,47,107,0.55), transparent 75%),
      radial-gradient(ellipse 130px 140px at 640px 640px, rgba(106,74,34,0.6), transparent 75%),
      radial-gradient(ellipse 260px 200px at 1100px 120px, rgba(60,120,50,0.45), transparent 75%),
      radial-gradient(ellipse 300px 220px at 300px 80px, rgba(50,70,40,0.4), transparent 75%),
      linear-gradient(180deg, #141a12 0%, var(--ink-night) 100%);
  }
  .info-section {
    position: absolute;
    left: 42px;
    right: 30px;
    margin: 0;
    padding: 0;
    list-style: none;
    font-size: 13.4px;
    letter-spacing: 0.1px;
    white-space: nowrap;
  }
  .section-title {
    position: absolute;
    left: 42px;
    margin: 0;
    font-size: 13px;
    font-weight: 500;
    color: var(--heading-red);
  }
  .rules-title { top: 64px; }
  .guidelines-title { top: 410px; }
  .rules-list { top: 119px; line-height: 27.3px; }
  .guidelines-list { top: 459px; line-height: 25.8px; }
  .sub-item { padding-left: 34px; }
</style>
</head>
<body>
  <main class="flyer-back">
    <div class="sake-backdrop" role="img" aria-label="Softly lit photograph of sake bottles in green and blue glass with a small ceramic cup"></div>

    <h2 class="section-title rules-title">Contest Rules</h2>
    <ul class="info-section rules-list">
      <li>1. Winning recipes will become the property of Brimba Sketto and cannot be duplicated or resold anywhere else - winners will be credited on the menu</li>
      <li>2. All cocktail recipes must be original – be creative!</li>
      <li>3. Any ingredients will be considered; however, sake is a key component and there can be no ingredient with an alcohol content above 20%</li>
      <li>4. Top eight finalists will be contacted via email and phone on August 10th, 2015. If they do not respond with 48 hours, another finalist will be chosen in their place.</li>
      <li>5. From August 11th, 2015 - August 31st, 2015, voting for the three winners will take place in Brimba Sketto's restaurant.</li>
      <li>The three cocktails that receive the most votes from our customers will be chosen for the 1st, 2nd, and 3rd prizes.</li>
      <li>6. The final three winners will be contacted on August 31st, 2015.&nbsp; If they do not respond with 48 hours,</li>
      <li>the finalist with the next highest amount of votes will be chosen in their place.</li>
    </ul>

    <h2 class="section-title guidelines-title">Submission Guidelines</h2>
    <ul class="info-section guidelines-list">
      <li>1. Please include the following information:</li>
      <li class="sub-item">A. Name of the cocktail</li>
      <li class="sub-item">B. Ingredients list and measurements</li>
      <li class="sub-item">C. Detailed list of instructions</li>
      <li class="sub-item">D. Photo of the cocktail</li>
      <li class="sub-item">E. Any specific equipment/materials or glassware, if necessary</li>
      <li class="sub-item">F . Your name, the name of your restaurant, and the best way to contact you</li>
      <li>2. Submit all materials to brimbasket1@quillmarn.com - in the subject line include your name and the name of your cocktail</li>
      <li>3. If you have any questions, please contact us via email or our store number: 555-014-2297.</li>
    </ul>
  </main>
</body>
</html>
```